Wine Label Design

We are looking for a new label to add to our winery. This is to be named "Feldkamm" which is the German word for schoolhouse. Our tasting room is a one room school house built in 1887. I would like the label to be very simple and clean with a schoolhouse on the front. I would like to schoolhouse to be sketch style, not a cartoonish design. I have attached a photo of the schoolhouse that we pour from, this is what I would want the schoolhouse to resemble. I have also added a copy of our current "higher end" label so that you have an idea of our style. I would like the new label to be cohesive with our old label and look good next to each other on our shelves. Just as added clarification we do not want Kolber Vineyards on the new label - we want that replaced with Feldkamm. If you are unable to do a full label design we would also accept just the schoolhouse drawing design as well. Thank you.

Feldkamm

```html
<!DOCTYPE html>
<html lang="en">
<head>
<meta charset="utf-8">
<title>Feldkamm Wine Labels</title>
<link href="https://fonts.googleapis.com/css2?family=Bodoni+Moda:wght@400&family=Italianno&display=swap" rel="stylesheet">
<style>
  :root {
    --backdrop: #cbcbcb;
    --label-dark: #271c0a;
    --label-light: #ffffff;
    --ink-light: #ffffff;
    --ink-dark: #111111;
    --sketch-dark: #4a3d27;
    --sketch-light: #e6e6e6;
  }
  html, body {
    margin: 0;
    padding: 0;
    width: 1200px;
    height: 1000px;
    overflow: hidden;
    background: var(--backdrop);
  }
  .canvas {
    position: relative;
    width: 1200px;
    height: 1000px;
  }
  .label-shapes {
    position: absolute;
    left: 0;
    top: 0;
  }
  .label-text {
    position: absolute;
    top: 0;
    width: 489px;
    height: 1000px;
    text-align: center;
  }
  .label-text--rose { left: 91px; color: var(--ink-light); }
  .label-text--gewurz { left: 620px; color: var(--ink-dark); }
  .schoolhouse-art {
    position: absolute;
    left: 78px;
    top: 258px;
    width: 158px;
    height: 156px;
  }
  .label-text--rose .schoolhouse-art {
    background: linear-gradient(180deg, var(--sketch-dark), var(--label-dark));
  }
  .label-text--gewurz .schoolhouse-art {
    left: 164px;
    background: linear-gradient(180deg, var(--sketch-light), #f7f7f7);
  }
  .label-text--rose .schoolhouse-art { left: 158px; }
  .brand-name {
    position: absolute;
    left: 0; right: 0;
    top: 432px;
    margin: 0;
    font-family: "Bodoni Moda", "Didot", serif;
    font-weight: 400;
    font-size: 64px;
    line-height: 1;
  }
  .vintage {
    position: absolute;
    left: 0; right: 0;
    top: 551px;
    font-family: "Bodoni Moda", "Didot", serif;
    font-size: 17px;
    letter-spacing: 5px;
    line-height: 1;
  }
  .varietal {
    position: absolute;
    left: 0; right: 0;
    top: 598px;
    font-family: "Italianno", cursive;
    font-size: 52px;
    line-height: 1;
  }
  .region {
    position: absolute;
    left: 0; right: 0;
    top: 704px;
    font-family: "Bodoni Moda", "Didot", serif;
    font-size: 16px;
    letter-spacing: 0.5px;
    line-height: 1;
  }
</style>
</head>
<body>
<div class="canvas">
  <svg class="label-shapes" width="1200" height="1000" viewBox="0 0 1200 1000" aria-hidden="true">
    <path d="M91,782 V269 Q335.5,213 580,269 V782 Z" fill="var(--label-dark)"/>
    <path d="M620,782 V269 Q864.5,213 1109,269 V782 Z" fill="var(--label-light)"/>
  </svg>

  <section class="label-text label-text--rose">
    <div class="schoolhouse-art" role="img" aria-label="Sketch-style line drawing of a one-room schoolhouse with shuttered doors"></div>
    <h1 class="brand-name">Feldkamm</h1>
    <div class="vintage">2016</div>
    <div class="varietal">Dry Rosé</div>
    <div class="region">FINGER LAKES</div>
  </section>

  <section class="label-text label-text--gewurz">
    <div class="schoolhouse-art" role="img" aria-label="Sketch-style line drawing of a one-room schoolhouse with shuttered doors"></div>
    <h1 class="brand-name">Feldkamm</h1>
    <div class="vintage">2016</div>
    <div class="varietal">Gewürztraminer</div>
    <div class="region">FINGER LAKES</div>
  </section>
</div>
</body>
</html>
```